we do all sorts of cleaning however bookings are limited!
why not chose the right cleaners for you!
pressure cleaning, window cleaning, office, end of lease clean, accommodation, industrial and commercial cleaning and house cleaning

Logo Text

Bright Nest Cleaning Service

```html
<!DOCTYPE html>
<html lang="en">
<head>
<meta charset="utf-8">
<title>Bright Nest Cleaning Service – Business Cards</title>
<link href="https://fonts.googleapis.com/css2?family=Roboto:wght@400;700;900&family=Open+Sans:wght@400;600&display=swap" rel="stylesheet">
<style>
  :root {
    --bg: #c9c9c9;
    --card: #000000;
    --edge: #1fb0ec;
    --blue: #16a9e9;
    --green: #8cc63f;
    --rule: #5c8a28;
    --white: #ffffff;
    --ink: #000000;
  }
  * { box-sizing: border-box; margin: 0; padding: 0; }
  html, body { width: 1200px; height: 802px; overflow: hidden; }
  body {
    background: var(--bg);
    display: flex; align-items: center; justify-content: center; gap: 50px;
    font-family: "Open Sans", Arial, sans-serif;
  }
  .card {
    position: relative;
    width: 540px; height: 310px;
    background: var(--card);
    border: 2px solid var(--edge);
    border-radius: 26px;
    overflow: hidden;
    color: var(--white);
  }
  .brand {
    display: flex; align-items: center; gap: 10px;
    font-family: "Roboto", Arial, sans-serif;
    font-weight: 900; color: var(--blue);
    line-height: 1.05;
  }
  .brand-dot { width: 16px; height: 16px; border-radius: 50%; background: var(--green); flex: none; }

  /* front */
  .card-front .brand { position: absolute; left: 34px; top: 126px; width: 240px; font-size: 26px; }
  .card-front .divider { position: absolute; left: 0; top: 0; width: 540px; height: 310px; }
  .contact { position: absolute; left: 300px; top: 48px; width: 225px; }
  .contact-name { font-family: "Roboto", Arial, sans-serif; font-weight: 700; font-size: 24px; color: var(--blue); line-height: 1.2; }
  .contact-role { font-family: Georgia, serif; font-size: 13px; margin: 2px 0 14px; }
  .contact-line { display: flex; align-items: center; gap: 9px; font-family: Georgia, serif; font-size: 13px; margin-bottom: 8px; white-space: nowrap; }
  .contact-line svg { width: 14px; height: 14px; flex: none; }
  .contact-address { font-family: Georgia, serif; font-size: 13px; line-height: 1.45; margin-top: 6px; white-space: nowrap; }

  /* back */
  .card-back .brand { justify-content: center; font-size: 34px; margin-top: 46px; white-space: nowrap; }
  .tagline {
    text-align: center; margin-top: 34px;
    font-family: "Roboto", Arial, sans-serif; font-weight: 700;
    font-size: 18px; color: var(--blue); white-space: nowrap;
  }
  .band {
    margin-top: 8px; background: var(--green); color: var(--ink);
    text-align: center; padding: 7px 0;
    font-family: "Roboto", Arial, sans-serif; font-weight: 700; font-size: 18px;
  }
  .services { text-align: center; margin: 14px 20px 0; font-size: 14px; line-height: 1.5; }
  .service-row { display: block; white-space: nowrap; }
  .services .sep { color: var(--blue); margin: 0 4px; }
</style>
</head>
<body>
  <section class="card card-front">
    <svg class="divider" viewBox="0 0 540 310" aria-hidden="true">
      <line x1="285" y1="20" x2="285" y2="290" stroke="#5c8a28" stroke-width="1"/>
    </svg>
    <div class="brand"><span class="brand-dot"></span><span>Bright Nest<br>Cleaning Service</span></div>
    <div class="contact">
      <div class="contact-name">Daniel Harper</div>
      <div class="contact-role">Owner</div>
      <div class="contact-line">
        <svg viewBox="0 0 16 16" aria-hidden="true"><path fill="#8cc63f" d="M3 1h3l1.5 4-2 1.3a9 9 0 0 0 4.2 4.2L11 8.5l4 1.5v3c0 1-1 2-2 2A12 12 0 0 1 1 3c0-1 1-2 2-2z"/></svg>
        (407) 555-0142
      </div>
      <div class="contact-line">
        <svg viewBox="0 0 16 16" aria-hidden="true"><rect x="1" y="3" width="14" height="10" fill="#8cc63f"/><path d="M1 3l7 6 7-6" fill="none" stroke="#000" stroke-width="1.2"/></svg>
        hello@brightnest.com
      </div>
      <div class="contact-line">
        <svg viewBox="0 0 16 16" aria-hidden="true"><circle cx="8" cy="8" r="7" fill="#8cc63f"/><path d="M1 8h14M8 1c-3 4-3 10 0 14M8 1c3 4 3 10 0 14" fill="none" stroke="#000" stroke-width="1"/></svg>
        www.brightnestclean.com
      </div>
      <div class="contact-address">88 Harbor Lane, Suite 4<br>32801, United States</div>
    </div>
  </section>

  <section class="card card-back">
    <div class="brand"><span class="brand-dot"></span>Bright Nest Cleaning Service</div>
    <p class="tagline">We do all sorts of cleaning however bookings are limited!</p>
    <p class="band">why not chose the right cleaners for you!</p>
    <p class="services">
      <span class="service-row"><span class="sep">•</span>Pressure cleaning <span class="sep">•</span> Window Cleaning <span class="sep">•</span> Office <span class="sep">•</span> End of lease clean</span>
      <span class="service-row"><span class="sep">•</span>Accommodation <span class="sep">•</span> Industrial and Commercial Cleaning and</span>
      <span class="service-row">house cleaning</span>
    </p>
  </section>
</body>
</html>
```